Real Estate Design Website

I would like to have a design for "real estate agent" website. It needs to be in a "Responsive" framework.

The design need to be suitable for different viewer from all around the world. It needs to be modern. It'd be great if there is a design for mobile and vexo/tablet (it's all under responsive framework). It needs to be easy to navigate and look modern

Target Market(s)

End user/Real estate buyers from different part of the world

Industry/Entity Type

Real Estate

Requirements
Must have
• It's for real estate agent website which is used to represent their brand/image but at the same time it also for their client which is real estate buyers
Should not have
• Should not be boring design/out of date

```html
<!DOCTYPE html>
<html lang="en">
<head>
<meta charset="utf-8">
<title>Realestate Company – Home</title>
<link href="https://fonts.googleapis.com/css2?family=Arimo:wght@400;700&family=Tinos&display=swap" rel="stylesheet">
<style>
:root{
  --page:#e9edf2;
  --blue:#3b78c2;
  --blue-dark:#2d63a6;
  --blue-mid:#4a86cc;
  --blue-light:#6aa3dc;
  --panel:#4f8bd0;
  --footer:#4677b5;
  --footer-text:#dbe7f5;
  --nav-text:#333;
  --band-top:#eefcfd;
  --band-bottom:#c9eff2;
  --ink:#333;
  --link-blue:#2f6db4;
  --white:#fff;
  --orange:#f7871f;
  --orange-light:#ffa64a;
}
*{box-sizing:border-box;margin:0;padding:0}
html,body{width:726px;height:1200px;overflow:hidden;background:var(--page)}
body{font-family:"Arimo",Arial,sans-serif;color:var(--ink);position:relative}
.site{position:absolute;left:0;top:0;width:726px;height:1200px;overflow:hidden;background:var(--white)}
.abs{position:absolute}

/* header */
.header{left:0;top:0;width:726px;height:83px;background:linear-gradient(180deg,#3f7dc6,#3770b4)}
.brand{left:10px;top:15px;display:flex;align-items:center;gap:8px}
.brand-square{width:18px;height:18px;background:var(--white)}
.brand-name{font-family:"Arimo",Arial,sans-serif;font-weight:400;font-size:21px;color:var(--white);line-height:1}
.brand-tag{left:34px;top:48px;font-size:11px;color:var(--white)}
.call{right:8px;top:50px;font-family:"Tinos",Georgia,serif;font-size:18px;color:var(--white)}

/* nav */
.nav{left:0;top:83px;width:726px;height:31px;background:linear-gradient(180deg,#e6e6e6,#cfcfcf);display:flex;padding-left:11px}
.nav a{font-size:12px;color:var(--nav-text);text-decoration:none;padding:0 13px;line-height:31px;height:31px}
.nav a.is-active{background:var(--blue-mid);color:var(--white);border-radius:6px 6px 0 0;margin-top:3px;line-height:28px;height:28px}

/* hero */
.hero{left:0;top:114px;width:726px;height:293px;background:linear-gradient(180deg,#3d7ccb,#2f69b2)}
.slide{left:9px;top:17px;width:375px;height:250px;background:#d6e3f2;padding:6px}
.slide-photo{width:100%;height:100%;background:linear-gradient(180deg,#4a9ae0 0%,#8fc3ef 35%,#b08a57 55%,#6c9a3c 80%,#4f7d2b 100%)}
.slide-caption{left:15px;top:208px;width:363px;height:53px;background:rgba(40,90,160,.92);padding:9px 19px}
.slide-caption h2{font-weight:400;font-size:15px;color:var(--white)}
.slide-caption p{font-size:10px;color:var(--white);margin-top:5px}
.dots{left:150px;top:273px;display:flex;gap:4px}
.dots span{width:6px;height:6px;border-radius:50%;background:var(--white)}
.dots span.off{background:#2a5d9e}

.search{left:407px;top:17px;width:310px;height:275px}
.tab{top:0;height:31px;border-radius:7px 7px 0 0;font-size:16px;font-weight:700;text-align:center;line-height:31px}
.tab-tenants{left:0;width:121px;background:var(--panel);color:var(--white)}
.tab-owners{left:125px;width:97px;background:#8ebfee;color:var(--white)}
.search-body{left:0;top:31px;width:310px;height:240px;background:var(--panel);border-radius:0 6px 6px 6px;padding:0 15px}
.label{font-size:12px;color:var(--white)}
.field{background:var(--white);border-radius:3px;font-size:12px;color:#557;padding-left:14px;line-height:31px;height:35px;border:2px solid #c8dcf2}
.select{background:var(--white);border-radius:2px;font-size:10px;color:#4a6fa0;padding-left:15px;height:23px;line-height:23px;width:150px}
.select svg{position:absolute;right:6px;top:6px}
.check{width:11px;height:11px;background:var(--white);border-radius:2px}
.btn-search{left:125px;top:187px;width:155px;height:32px;border:2px solid #b9d6f3;border-radius:6px;background:linear-gradient(180deg,#6aa8e6,#3c7fcb);color:var(--white);font-size:16px;text-align:center;line-height:28px}

/* services band */
.band{left:0;top:407px;width:726px;height:118px;background:linear-gradient(180deg,var(--band-top),var(--band-bottom))}
.service{top:12px;width:215px}
.service h3{display:flex;align-items:center;gap:6px;font-weight:400;font-size:16px;color:var(--link-blue)}
.service p{font-size:9px;line-height:16.2px;color:#444;margin-top:6px}

/* listing grid */
.card{width:164px;height:149px;background:#dfe4ea;padding:4px}
.card-photo{width:100%;height:100px}
.card-caption{position:absolute;left:0;bottom:0;width:164px;height:40px;background:var(--blue-mid);color:var(--white);padding:4px 8px}
.card-caption b{display:block;font-weight:400;font-size:12px}
.card-caption span{font-size:10px}
.card-caption svg{position:absolute;right:8px;top:9px}

/* member area */
.members{left:0;top:876px;width:726px;height:145px;background:linear-gradient(180deg,#4d88cc,#3c77bd)}
.box{top:10px;height:82px;border:1px solid #8fb7e3;border-radius:3px;background:rgba(255,255,255,.07)}
.box h4{position:absolute;left:18px;top:8px;font-weight:400;color:var(--white)}
.input{top:42px;height:24px;background:var(--white);border-radius:2px;font-size:12px;color:#4a6fa0;padding-left:8px;line-height:24px}
.btn{top:41px;height:26px;border:2px solid #b9d6f3;border-radius:5px;background:linear-gradient(180deg,#6aa8e6,#3c7fcb);color:var(--white);font-size:12px;text-align:center;line-height:22px}
.join{left:9px;top:101px;width:349px;height:34px;border-radius:3px;overflow:hidden;background:linear-gradient(180deg,#78aee6,#4d8bd0)}
.join span{position:absolute;left:35px;top:8px;font-size:16px;color:var(--white)}
.join-cta{position:absolute;right:0;top:0;width:135px;height:34px;background:linear-gradient(180deg,var(--orange-light),var(--orange));clip-path:polygon(0 0,100% 0,100% 100%,0 100%,12px 50%)}
.join-cta b{position:absolute;left:26px;top:7px;font-weight:400;font-size:17px;color:var(--white)}
.social{top:103px;width:32px;height:32px;border-radius:4px}

/* footer */
.footer{left:0;top:1021px;width:726px;height:179px;background:var(--footer)}
.fcol{top:15px}
.fcol h5{font-size:12px;color:var(--white);margin-bottom:9px}
.fcol a{display:block;font-size:9.5px;color:var(--footer-text);text-decoration:none;line-height:16.2px}
.fcol p{font-size:9.5px;color:var(--footer-text);line-height:16.2px;width:236px}
.fcol strong{display:block;font-size:9.5px;color:var(--white);line-height:16.2px}
.pager{display:inline-block;width:10px;height:10px;border-radius:50%;background:#8eb1d9;margin-left:4px;vertical-align:-1px}
.fbrand{left:546px;top:16px;display:flex;align-items:center;gap:6px}
.fbrand i{width:11px;height:11px;background:var(--white);display:block}
.fbrand span{font-family:"Arimo",Arial,sans-serif;font-weight:400;font-size:13px;color:var(--white)}
</style>
</head>
<body>
<div class="site">

  <header class="header abs">
    <div class="brand abs"><span class="brand-square"></span><span class="brand-name">Realestate Company</span></div>
    <div class="brand-tag abs">Lorem Ipsum is simply dummy text</div>
    <div class="call abs">Call us: (555) 014-2286</div>
  </header>

  <nav class="nav abs">
    <a href="#">Home</a><a href="#" class="is-active">Our Story</a><a href="#">Tenant</a><a href="#">Owner</a><a href="#">Buying</a><a href="#">Contact us</a>
  </nav>

  <section class="hero abs">
    <div class="slide abs">
      <div class="slide-photo" role="img" aria-label="Photo of a two-storey family house with a for-sale sign on the front lawn"></div>
    </div>
    <div class="slide-caption abs">
      <h2>Lorem Ipsum is simply dummy text of</h2>
      <p>We work with investors to make managing your investments easy!</p>
    </div>
    <div class="dots abs"><span></span><span></span><span class="off"></span><span></span><span></span></div>

    <form class="search abs">
      <div class="tab tab-tenants abs">Tenants</div>
      <div class="tab tab-owners abs">Oweners</div>
      <div class="search-body abs">
        <div class="label abs" style="left:30px;top:18px">Address, Suburbs, Postcodes, or Regions</div>
        <div class="field abs" style="left:30px;top:41px;width:253px">Example: Harbor Falls, Westmark 40512</div>
        <div class="check abs" style="left:40px;top:87px">
          <svg width="11" height="11" viewBox="0 0 11 11"><path d="M2 5.5l2.5 2.5L9 2.5" fill="none" stroke="#2f6db4" stroke-width="2"/></svg>
        </div>
        <div class="label abs" style="left:57px;top:86px">Include surrounding suburbs</div>
        <div class="label abs" style="left:34px;top:118px">Property Type :</div>
        <div class="select abs" style="left:131px;top:114px">Select one
          <svg width="8" height="11" viewBox="0 0 8 11"><path d="M4 0l4 4H0zM4 11L0 7h8z" fill="#333"/></svg></div>
        <div class="label abs" style="left:53px;top:155px">Bedrooms :</div>
        <div class="select abs" style="left:131px;top:151px">Select one
          <svg width="8" height="11" viewBox="0 0 8 11"><path d="M4 0l4 4H0zM4 11L0 7h8z" fill="#333"/></svg></div>
        <div class="btn-search abs">Search</div>
      </div>
    </form>
  </section>

  <section class="band abs">
    <div class="service abs" style="left:9px">
      <h3><svg width="22" height="19" viewBox="0 0 22 19"><path d="M11 1L1 10h3v8h14v-8h3z" fill="#2f6db4"/></svg>Buy a home</h3>
      <p>Lorem Ipsum is simply dummy text of the printing and typesetting industry. Lorem Ipsum has been the industry's standard dummy text ever since the 1500s, when an unknown</p>
    </div>
    <div class="service abs" style="left:256px">
      <h3><svg width="22" height="19" viewBox="0 0 22 19"><path d="M11 1L1 10h3v8h14v-8h3z" fill="#2f6db4"/></svg>Sell a home</h3>
      <p>Lorem Ipsum is simply dummy text of the printing and typesetting industry. Lorem Ipsum has been the industry's standard dummy text ever since the 1500s, when an</p>
    </div>
    <div class="service abs" style="left:506px;width:212px">
      <h3><svg width="22" height="19" viewBox="0 0 22 19"><path d="M11 1L1 10h3v8h14v-8h3z" fill="#2f6db4"/></svg>Rent a home</h3>
      <p>Lorem Ipsum is simply dummy text of the printing and typesetting industry. Lorem Ipsum has been the industry's standard dummy text ever since the 1500s, when an unknown printer took</p>
    </div>
  </section>

  <!-- listings row 1 -->
  <article class="card abs" style="left:9px;top:541px">
    <div class="card-photo" role="img" aria-label="Photo of a resort apartment block beside a pool" style="background:linear-gradient(180deg,#7fb3e6,#c9a98a 55%,#6d8d5a)"></div>
    <div class="card-caption"><b>Lorem ipsum dolor sit</b><span>Ut enim ad minim</span><svg width="24" height="22" viewBox="0 0 24 22"><circle cx="9" cy="9" r="6.5" fill="none" stroke="#fff" stroke-width="2.5"/><path d="M14 13.5l7 6" stroke="#fff" stroke-width="3.5" stroke-linecap="round"/></svg></div>
  </article>
  <article class="card abs" style="left:191px;top:541px">
    <div class="card-photo" role="img" aria-label="Photo of a modern white villa with green roofs" style="background:linear-gradient(180deg,#5f9fd6,#a9c7a0 50%,#4f7a3a)"></div>
    <div class="card-caption"><b>Lorem ipsum dolor sit</b><span>Ut enim ad minim</span><svg width="24" height="22" viewBox="0 0 24 22"><circle cx="9" cy="9" r="6.5" fill="none" stroke="#fff" stroke-width="2.5"/><path d="M14 13.5l7 6" stroke="#fff" stroke-width="3.5" stroke-linecap="round"/></svg></div>
  </article>
  <article class="card abs" style="left:373px;top:541px">
    <div class="card-photo" role="img" aria-label="Photo of colourful high-rise apartment towers" style="background:linear-gradient(180deg,#6fb0ea,#9dd3a8 60%,#5b9a55)"></div>
    <div class="card-caption"><b>Lorem ipsum dolor sit</b><span>Ut enim ad minim</span><svg width="24" height="22" viewBox="0 0 24 22"><circle cx="9" cy="9" r="6.5" fill="none" stroke="#fff" stroke-width="2.5"/><path d="M14 13.5l7 6" stroke="#fff" stroke-width="3.5" stroke-linecap="round"/></svg></div>
  </article>
  <article class="card abs" style="left:554px;top:541px">
    <div class="card-photo" role="img" aria-label="Photo of a country path through green fields under a blue sky" style="background:linear-gradient(180deg,#2f7fd4,#9fcdf2 55%,#5aa23a 70%,#3f8a2a)"></div>
    <div class="card-caption"><b>Lorem ipsum dolor sit</b><span>Ut enim ad minim</span><svg width="24" height="22" viewBox="0 0 24 22"><circle cx="9" cy="9" r="6.5" fill="none" stroke="#fff" stroke-width="2.5"/><path d="M14 13.5l7 6" stroke="#fff" stroke-width="3.5" stroke-linecap="round"/></svg></div>
  </article>

  <!-- listings row 2 -->
  <article class="card abs" style="left:9px;top:706px">
    <div class="card-photo" role="img" aria-label="Photo of a large cream-coloured suburban house" style="background:linear-gradient(180deg,#4c8fdb,#e7dcc0 55%,#8a8a7a)"></div>
    <div class="card-caption"><b>Lorem ipsum dolor sit</b><span>Ut enim ad minim</span><svg width="24" height="22" viewBox="0 0 24 22"><circle cx="9" cy="9" r="6.5" fill="none" stroke="#fff" stroke-width="2.5"/><path d="M14 13.5l7 6" stroke="#fff" stroke-width="3.5" stroke-linecap="round"/></svg></div>
  </article>
  <article class="card abs" style="left:191px;top:706px">
    <div class="card-photo" role="img" aria-label="Photo of a cluster of white residential towers with palm trees" style="background:linear-gradient(180deg,#3c6fc0,#d8d8e0 55%,#4d7d48)"></div>
    <div class="card-caption"><b>Lorem ipsum dolor sit</b><span>Ut enim ad minim</span><svg width="24" height="22" viewBox="0 0 24 22"><circle cx="9" cy="9" r="6.5" fill="none" stroke="#fff" stroke-width="2.5"/><path d="M14 13.5l7 6" stroke="#fff" stroke-width="3.5" stroke-linecap="round"/></svg></div>
  </article>
  <article class="card abs" style="left:373px;top:706px">
    <div class="card-photo" role="img" aria-label="Photo of a two-storey house on a green lawn" style="background:linear-gradient(180deg,#c9dff0,#8aa07a 50%,#6d9a3f)"></div>
    <div class="card-caption"><b>Lorem ipsum dolor sit</b><span>Ut enim ad minim</span><svg width="24" height="22" viewBox="0 0 24 22"><circle cx="9" cy="9" r="6.5" fill="none" stroke="#fff" stroke-width="2.5"/><path d="M14 13.5l7 6" stroke="#fff" stroke-width="3.5" stroke-linecap="round"/></svg></div>
  </article>
  <article class="card abs" style="left:554px;top:706px">
    <div class="card-photo" role="img" aria-label="Photo of white high-rise towers beside a park" style="background:linear-gradient(180deg,#8fc0ea,#e6eef4 50%,#5c9a4c)"></div>
    <div class="card-caption"><b>Lorem ipsum dolor sit</b><span>Ut enim ad minim</span><svg width="24" height="22" viewBox="0 0 24 22"><circle cx="9" cy="9" r="6.5" fill="none" stroke="#fff" stroke-width="2.5"/><path d="M14 13.5l7 6" stroke="#fff" stroke-width="3.5" stroke-linecap="round"/></svg></div>
  </article>

  <section class="members abs">
    <div class="box abs" style="left:9px;width:349px">
      <h4 style="font-size:18px">Member login</h4>
      <div class="input abs" style="left:18px;width:111px">User name</div>
      <div class="input abs" style="left:141px;width:111px">Password</div>
      <div class="btn abs" style="left:262px;width:70px">Login</div>
    </div>
    <div class="box abs" style="left:369px;width:348px">
      <h4 style="font-size:15px;top:10px">Subscribe to our weekly newsletter</h4>
      <div class="input abs" style="left:16px;width:229px">email address</div>
      <div class="btn abs" style="left:253px;width:80px">Subscribe</div>
    </div>
    <div class="join abs"><span>Not a member yet</span><div class="join-cta"><b>Signup Now</b></div></div>
    <div class="social abs" style="left:372px;background:#3d64a8" role="img" aria-label="Social network link"></div>
    <div class="social abs" style="left:419px;background:#39b4ea" role="img" aria-label="Social network link"></div>
    <div class="social abs" style="left:465px;background:#333" role="img" aria-label="Social network link"></div>
  </section>

  <footer class="footer abs">
    <div class="fcol abs" style="left:17px">
      <h5>About Us</h5>
      <a href="#">About us</a><a href="#">Why us</a><a href="#">Customer Stories</a><a href="#">Press Resources</a><a href="#">Press Releases</a><a href="#">Contact us</a>
    </div>
    <div class="fcol abs" style="left:156px">
      <h5>Properties</h5>
      <a href="#">Rent a home</a><a href="#">Lease a home</a><a href="#">Buy a home</a><a href="#">Sell a home</a><a href="#">Ask advices</a>
    </div>
    <div class="fcol abs" style="left:296px">
      <h5>Costamer Testimonials <span class="pager"></span><span class="pager"></span></h5>
      <p>Lorem Ipsum is simply dummy text of the printing and typesetting industry. Lorem Ipsum has been the industr standard dummy text ever since the 1500s, when an unknown printer took a</p>
      <strong>Lorem Ipsum is simply</strong>
      <strong>Owner, Lorem Ipsum</strong>
    </div>
    <div class="fbrand abs"><i></i><span>Realestate company</span></div>
  </footer>

</div>
</body>
</html>
```